Label design for ecological olive oil from an innovative farm in Spain

EL PRADO SOLAR - Olive Oil Label
El Prado Solar is a small farm in southern Spain dedicated to regenerative, ecological and syntropic agriculture. We are launching a new extra virgin olive oil and, alongside it, a renewed brand identity that reflects our relationship with land, life and earth.
Our farm works as a living food forest: diverse, dense, colourful and abundant. This is not industrial organic farming — it is ecosystem regeneration in action. We are looking for a label that feels:
* Lush, abundant and alive
* Nature-connected and animist (the land as a living being)
* Sunny Mediterranean (southern Spain, warmth, light, joy)
* Upbeat and playful, not austere or “eco-serious”
* Slightly rebellious, non-corporate, non-industrial
This is an olive oil for people who care deeply about the planet, but who also love beauty, colour and pleasure.
We are particularly drawn to designs that express the visual richness and lushness of our syntropic food forest:
* Dense, layered plant life
* Multiple tree species growing together
* A sense of abundance
* A “window into a living world” feeling
Tree species present on the farm include:
* Olive
* Citrus
* Pomegranate
* Fig
* Almond
We welcome designs with illustrative approaches that feel hand-drawn, painterly or slightly retro. We are open to interpretation — the goal is to transmit aliveness, not literal realism.
We currently use Montserrat font and are happy to continue with it or something similar.
We are also open to retro-inspired or softer typefaces, provided they feel natural, warm and not corporate.
We want to avoid plastic labels. The design should work with:
* Uncoated/organic paper labels, or
* Direct printing or screen printing onto glass
The label should feel tactile and natural.
We have uploaded :
* Final front and back label text (Spanish + English)
* Logo
* Reference images (AI explorations, farm photos, landscape, food forest)
The olive oil will be sold in Spain and internationally, so bilingual clarity is important.
Our business logo should be used but does not need to dominate the front label.
It may work better subtly placed, possibly on the back label or integrated quietly into the design.
A successful label will feel like:
* A living landscape captured on a bottle
* Something joyful, rooted and contemporary
* A product of land, care and imagination — not marketing
We want people to feel, instinctively:
This oil comes from a place that is alive.

```html
<!DOCTYPE html>
<html lang="es">
<head>
<meta charset="utf-8">
<title>El Prado Solar – Etiquetas de aceite</title>
<link href="https://fonts.googleapis.com/css2?family=Montserrat:wght@400;500;600;700&display=swap" rel="stylesheet">
<style>
  :root{
    --page:#f7f6f1;
    --paper:#efece2;
    --olive-dark:#4b4a1c;
    --olive:#7f7d22;
    --olive-mid:#a7a54c;
    --olive-soft:#b3b283;
    --gold:#b59a4a;
    --rule:#8d8b5a;
    --white:#ffffff;
  }
  *{box-sizing:border-box;margin:0;padding:0}
  html,body{width:850px;height:1200px;overflow:hidden}
  body{background:var(--page);font-family:"Montserrat",Arial,sans-serif;position:relative}

  .neck-band{position:absolute;top:40px;width:200px;height:62px;background:var(--white);
    border-radius:4px;display:flex;align-items:center;justify-content:center;gap:8px;
    box-shadow:0 1px 3px rgba(0,0,0,.08)}
  .neck-band--front{left:137px}
  .neck-band--back{left:513px}
  .brand-name{color:var(--gold);font-weight:600;letter-spacing:.5px;white-space:nowrap}
  .brand-dot{width:7px;height:7px;border-radius:50%;background:var(--gold);flex:none}
  .neck-band .brand-name{font-size:16px}

  .label{position:absolute;top:122px;width:330px;height:1048px;background:var(--paper);
    border-radius:165px;overflow:hidden;text-align:center;box-shadow:0 2px 8px rgba(0,0,0,.08)}
  .label--front{left:72px}
  .label--back{left:448px}

  /* Front */
  .front-brand{position:absolute;top:120px;left:0;right:0;display:flex;justify-content:center;align-items:center;gap:6px}
  .front-brand .brand-name{font-size:15px}
  .product-title{position:absolute;left:0;right:0;color:var(--olive-dark);font-weight:700;font-size:27px;line-height:36px}
  .product-title--es{top:200px}
  .product-title--en{top:285px}
  .rule{position:absolute;left:50px;right:50px;height:1px;background:var(--rule)}
  .rule--title{top:284px}
  .rule--claim{top:426px}
  .claim{position:absolute;left:30px;right:30px;color:var(--olive);font-weight:600;font-size:13px;line-height:17px}
  .claim--es{top:388px}
  .claim--en{top:432px}
  .volume{position:absolute;top:482px;left:50%;transform:translateX(-50%);background:var(--olive-mid);
    color:var(--white);font-weight:600;font-size:13px;padding:3px 9px;border-radius:12px}
  .forest-window{position:absolute;top:520px;left:12px;width:306px;height:515px;border-radius:140px;
    background:radial-gradient(ellipse at 50% 35%,#e6dc86 0%,#9aa13c 30%,#4f6a22 62%,#2f4717 85%)}

  /* Back */
  .back-brand{position:absolute;top:200px;left:0;right:0;display:flex;justify-content:center;align-items:center;gap:8px}
  .back-brand .brand-name{font-size:24px}
  .category{position:absolute;top:318px;left:40px;right:40px;color:var(--olive);font-weight:500;font-size:12.5px;line-height:15px}
  .origin{position:absolute;top:418px;left:48px;right:48px;height:56px;background:var(--olive-mid);
    border-radius:28px;color:var(--white);font-size:13px;line-height:17px;padding-top:10px}
  .origin strong{font-weight:600}
  .story-panel{position:absolute;top:476px;left:28px;right:28px;bottom:30px;border-radius:0 0 140px 140px;
    background:linear-gradient(to bottom,var(--paper) 0%,#c9c8a3 18%,var(--olive-soft) 45%,#a9a877 100%)}
  .story{position:absolute;left:24px;right:24px;color:var(--olive-dark);font-weight:500;font-size:12.8px;line-height:16.5px}
  .story--es{top:30px}
  .story--en{top:226px}
  .details{position:absolute;top:404px;left:14px;right:14px;color:var(--olive-dark);font-weight:600;font-size:7.6px;line-height:10px}
</style>
</head>
<body>

  <div class="neck-band neck-band--front"><span class="brand-dot"></span><span class="brand-name">EL PRADO SOLAR</span></div>
  <div class="neck-band neck-band--back"><span class="brand-dot"></span><span class="brand-name">EL PRADO SOLAR</span></div>

  <section class="label label--front">
    <div class="front-brand"><span class="brand-dot"></span><span class="brand-name">EL PRADO SOLAR</span></div>
    <h1 class="product-title product-title--es">Aceite de Oliva<br>Virgen Extra</h1>
    <div class="rule rule--title"></div>
    <h2 class="product-title product-title--en">Extra Virgin<br>Olive Oil</h2>
    <p class="claim claim--es">Cultivado con practicas de la<br>agricultura regenerativa y sintrópica</p>
    <div class="rule rule--claim"></div>
    <p class="claim claim--en">Grown using regenerative and<br>syntropic farming practices</p>
    <span class="volume">500ml</span>
    <div class="forest-window" role="img" aria-label="Illustration: a sunlit food forest of olive and citrus trees framed by a wreath of leaves, oranges and pomegranates"></div>
  </section>

  <section class="label label--back">
    <div class="back-brand"><span class="brand-dot"></span><span class="brand-name">EL PRADO SOLAR</span></div>
    <p class="category">Aceite de oliva de categoría superior obtenido directamente de aceitunas y solo mediante procedimientos mecánicos.</p>
    <div class="origin">Origen:<br><strong>Valdesol, Granada, España</strong></div>
    <div class="story-panel">
      <p class="story story--es">Edición limitada de la finca única<br>Elaborado y envasado por:<br>Fundación El Prado Solar<br>Proyecto agrícola dedicado a la regeneración de ecosistemas y al cuidado de la tierra y las personas.<br>Recolectado a mano<br>Prensado en frio, menos de un día tras la cosecha</p>
      <p class="story story--en">Limited edition from a single farm<br>Produced and bottled by:<br>Fundación El Prado Solar<br>An agricultural project dedicated to ecosystem regeneration and the care of land and people.<br>Hand picked and cold pressed within one day of harvest</p>
      <p class="details">Variedad: Picual · Manzanilla · Acebuche (Wild Olive)<br>Sin filtrar<br>Conservar en lugar fresco y protegido de la luz.<br>Lote: Otoño 2025<br>Consumir preferentemente antes de: 05/2027</p>
    </div>
  </section>

</body>
</html>
```